依頼概要
薬局内で製造・販売している薬のラベルシールの作成をお願いします。

■依頼の目的/概要
弊社は茨城県で調剤薬局を6店舗展開し、「いつもあなたのそばに」をモットーに、いつでも気軽に相談していただける薬局を目指して、業務を行っております。
このたび創業20周年を機に、薬局製剤ラベルのリニューアルを行います。
どうぞよろしくお願いします。

■依頼の詳細
内服薬3種類(かぜ薬、ビタミン剤、整腸剤)のラベルシールの作成

銀色のジップ付きアルミ袋にラベルを貼って販売しており、その形を継続します。
今までのイメージカラーを引き継ぎたいと考えております。
ラベルには商品名、効能、包数、のほかに各販売店舗名、法人名、住所を入れる必要があります。
テキストが編集できるような状態で納品ください。

【ラベルサイズ】
140mm×100mm

【デザインに対するイメージの希望】
あまり重厚な感じではなくて良いですが、お薬ですので、信頼感のある、効果があることがイメージできるものをお願いします。

■その他・参考事項
各商品の販売価格は、1200~1600円程度です。
現在の各商品のラベル等詳細についてはファイルに添付します。
イメージカラー等はそちらをご参考下さい。
ご提案頂いている皆様、ありがとうございます。
デザインいただくイメージとして販売ターゲット像をお示しします。

販売ターゲットは35歳女性。結婚し、8歳と1歳の二人の子供がいるが仕事もしており、自分のことは後回しになりがち。下の子供が風邪で病院にかかり薬局へ処方箋を持っていたところ、処方箋なしで買える薬局製剤を目にする。風邪気味で疲れもあった自分用に風邪薬とビタミンを買い、お腹をこわしやすい上の子供用に整腸剤も購入した。薬のデザインは癒し感があるし、風邪薬は夫が風邪気味の時にも使えるし、家庭の常備薬としても良いと思う。

初めに現在のラベルをお示ししてしまったので先入観が出てしまいがちであったかと思います。今後初めてご覧になる方は現在のラベルの写真を入れないファイルを添付いたしましたので、そちらをご覧ください。
どうぞよろしくお願いします。
■ 選んだ理由

白ベースでスッキリしたデザインに信頼感と薬の効果を感じました。
また、曲線のラインと、光が差し込んでいるような地の薄い斜めの模様から癒しも感じられ、こちらに決定させていただきました。

■ 提案者全員のお礼・コメント

多くの皆様にご参加いただき、誠にありがとうございました。
初めてのコンペであり不安がありましたが、数多くのご提案を頂きましたこと、感謝申し上げます。

```html
<!DOCTYPE html>
<html lang="ja">
<head>
<meta charset="UTF-8">
<title>かぜ薬 ラベル</title>
<link rel="stylesheet" href="https://fonts.googleapis.com/css2?family=M+PLUS+Rounded+1c:wght@400;500;700&display=swap">
<style>
  :root {
    --paper: #f2f0ec;
    --ink: #2b2b2b;
    --red: #e12a2f;
    --fruit-light: #f7a07a;
    --fruit-deep: #e6452f;
    --grey-dot: #3a3a3a;
  }
  html, body {
    margin: 0;
    padding: 0;
    width: 857px;
    height: 1200px;
    overflow: hidden;
  }
  body {
    font-family: "M PLUS Rounded 1c", sans-serif;
    color: var(--ink);
  }
  .label {
    position: relative;
    width: 857px;
    height: 1200px;
    background: var(--paper);
    overflow: hidden;
  }
  .header {
    position: absolute;
    top: 42px;
    left: 86px;
    font-size: 28px;
    font-weight: 700;
    letter-spacing: 6px;
    white-space: nowrap;
    line-height: 1.2;
  }
  .header .kind { color: var(--red); }
  .header .count { margin-left: 22px; }
  .illustration {
    position: absolute;
    left: 157px;
    top: 157px;
    width: 430px;
    height: 415px;
    border-radius: 12px;
    background: linear-gradient(135deg, var(--fruit-light) 0%, var(--fruit-deep) 100%);
  }
  .symptoms {
    position: absolute;
    top: 712px;
    left: 0;
    width: 100%;
    text-align: center;
    color: var(--red);
    font-size: 32px;
    font-weight: 700;
    letter-spacing: 6px;
    line-height: 1.2;
  }
  .product-name {
    position: absolute;
    top: 780px;
    left: 0;
    width: 100%;
    text-align: center;
    color: var(--red);
    font-size: 104px;
    font-weight: 700;
    letter-spacing: 44px;
    text-indent: 44px;
    line-height: 1;
  }
  .rule { position: absolute; left: 86px; top: 923px; }
  .stores {
    position: absolute;
    top: 998px;
    left: 170px;
    font-size: 28px;
    font-weight: 700;
    letter-spacing: 8px;
    line-height: 1.2;
    white-space: nowrap;
  }
  .stores .second { position: absolute; left: 287px; top: 0; }
  .wave { position: absolute; left: 86px; top: 1054px; }
  .company {
    position: absolute;
    top: 1079px;
    left: 195px;
    display: flex;
    align-items: center;
    gap: 24px;
  }
  .company .dot {
    width: 36px;
    height: 36px;
    border-radius: 50%;
    background: var(--grey-dot);
  }
  .company .name { font-size: 24px; font-weight: 500; letter-spacing: 1px; line-height: 1.2; }
  .company .address { font-size: 14px; margin-top: 6px; letter-spacing: 0.5px; }
</style>
</head>
<body>
  <div class="label">
    <div class="header">もみじ薬局<span class="kind">調剤薬</span><span class="count">18包入</span></div>

    <div class="illustration" role="img" aria-label="赤い水彩風のあんずの実のイラスト"></div>

    <div class="symptoms">発熱、鼻水、せき、のどの痛み</div>
    <div class="product-name">かぜ薬</div>

    <svg class="rule" width="685" height="8" viewBox="0 0 685 8">
      <line x1="0" y1="4" x2="685" y2="4" stroke="var(--red)" stroke-width="4"/>
    </svg>

    <div class="stores"><span>もみじ薬局</span><span class="second">〇〇〇薬局</span></div>

    <svg class="wave" width="685" height="16" viewBox="0 0 685 16">
      <path d="M0 8 Q 43 2 86 8 T 172 8 T 258 8 T 344 8 T 430 8 T 516 8 T 602 8 T 685 8" fill="none" stroke="var(--red)" stroke-width="3"/>
    </svg>

    <div class="company">
      <div class="dot"></div>
      <div>
        <div class="name">法人名法人名法人名法人名</div>
        <div class="address">〒0000-000住所が入ります住所が入ります住所が入ります</div>
      </div>
    </div>
  </div>
</body>
</html>
```